Need Instructors for martial arts school - special flyers to help

We are a kung fu and tai chi martial arts school and we need to appeal to a certain demographic - 16-30, driven, fit, personable - who can join our team of instructors to help grow our school. We envisage this flyer as as roughly between A6 and A7 in size. The kind of thing we can hand to some one we meet and they can easily stick it in a pocket but not so small it gets lost like a business card. We are a professional and serious organisation so don't want to go too dramatic or cheesy to get attention but the design needs to capture the attention of the reader quickly and keep them engaged. Martial arts has quite a bit of material to use for this purpose. NOTE: we are not Karate or Tae Kwon Do - the difference matters. We will upload our current logo and the text we want to use is this for the front:
"Challenge Yourself...
Teaching is the highest form of learning. Be a part of a professional, dedicated team, delivering the highest level Kung Fu...
Copper Heron Martial Arts"
On the back side it should say:
"Seeking martial arts instructors!
We train in one of the world's most effective martial art systems, Choy Li Fut Kung Fu. As an instructor, you will teach both beginner and intermediate level Kung Fu skills to adults and children at Copper Heron Martial Arts, Brisbane's premier martial arts school.
As an instructor, you will:
- Teach fundamentals to children and adults of all ages and abilities
- Progress student's martial arts and life skills
- Deliver fun and engaging classes
- Develop and grow your martial arts skills at an advanced level and pace
In return, you will receive your training tuition, which includes our high level instructor training program, until qualified and then a weekly one one on one with our very own Sifu, as well as one hour training sessions, twice a week , with our team.
At CHMA our motto is "Challenge yourself... for life!"
Contact us on 0417 863 120 to discuss your interest and suitability - ask for Sifu Rory."
There are two fonts we are liking right now for our designs, Merienda One and Red Rose from Google Fonts.
We basically need this to be cool enough to keep someone's attention and not have them throw it away before they have read it.
Info about us on copperheron.com.au

```html
<!DOCTYPE html>
<html lang="en">
<head>
<meta charset="utf-8">
<title>Copper Heron Martial Arts – Instructor Flyer</title>
<link rel="stylesheet" href="https://fonts.googleapis.com/css2?family=Merienda+One&family=Lato:ital,wght@0,400;0,700;1,700&display=swap">
<style>
:root{
  --stage:#a9a9a9;
  --red:#c8141d;
  --red-deep:#8e0b12;
  --ink:#111111;
  --charcoal:#2a2a2a;
  --white:#ffffff;
}
*{box-sizing:border-box;margin:0;padding:0}
html,body{width:1200px;height:1200px;overflow:hidden}
body{background:var(--stage);position:relative;font-family:"Lato",sans-serif}
.flyer{position:absolute;top:252px;width:527px;height:742px;overflow:hidden;color:var(--white)}
.flyer--front{left:53px;background:radial-gradient(ellipse at 50% 60%,#dcdcdc 0%,#8a8a8a 28%,#3a3a3a 55%,var(--ink) 85%)}
.flyer--back{left:619px;background:linear-gradient(100deg,var(--ink) 0%,var(--charcoal) 55%,#5a5a5a 100%)}
.band{position:absolute;left:0;width:100%;display:block}
.display{font-family:"Merienda One",cursive;line-height:1}

/* front */
.front__title{position:absolute;font-size:46px;text-transform:uppercase;letter-spacing:1px;white-space:nowrap}
.front__title--one{left:112px;top:22px}
.front__title--two{right:24px;top:82px}
.front__lead{position:absolute;top:208px;left:0;width:100%;text-align:center;font-family:"Merienda One",cursive;font-size:16.5px;line-height:1.3}
.emblem{position:absolute;left:121px;top:320px;width:288px;height:288px;border-radius:50%;background:var(--red);display:flex;align-items:center;justify-content:center;text-align:center;padding:40px;font-size:28px;line-height:1.2;color:var(--white)}
.vertical{position:absolute;writing-mode:vertical-rl;text-orientation:upright;font-size:30px;letter-spacing:2px;text-transform:uppercase;color:var(--white);line-height:1}
.v-copper{left:22px;top:318px}
.v-heron{left:58px;top:432px}
.v-arts{right:22px;top:330px}
.v-martial{right:58px;top:402px}
.front__web{position:absolute;left:20px;bottom:20px;display:flex;align-items:center;gap:10px;font-size:27px;white-space:nowrap}

/* back */
.back__seeking{position:absolute;left:26px;top:14px;font-size:54px;color:var(--red);text-transform:uppercase}
.back__role{position:absolute;left:26px;top:72px;font-size:29px;text-transform:uppercase;white-space:nowrap}
.back__intro{position:absolute;left:24px;top:118px;width:470px;font-size:15px;line-height:1.2}
.block{position:absolute;left:24px}
.block__heading{font-family:"Merienda One",cursive;font-size:17px;text-transform:uppercase;margin-bottom:3px}
.block ul{list-style:none;font-size:15px;line-height:1.18}
.block li{padding-left:11px;text-indent:-11px}
.block li::before{content:"• "}
.block--duties{top:224px;width:490px}
.block--rewards{top:400px;width:290px}
.photo{position:absolute;left:250px;top:372px;width:277px;height:300px;background:linear-gradient(160deg,#9a9a9a 0%,#d8d8d8 40%,#6e6e6e 100%);opacity:.75;-webkit-mask-image:linear-gradient(90deg,transparent 0%,#000 30%);mask-image:linear-gradient(90deg,transparent 0%,#000 30%)}
.motto{position:absolute;left:24px;top:564px;width:320px}
.motto__intro{font-size:18px}
.motto__line{font-family:"Merienda One",cursive;font-size:23px;text-transform:uppercase;line-height:1.1;margin-top:8px;white-space:nowrap}
.motto__line--red{color:var(--red);margin-left:6px;margin-top:0}
.badge{position:absolute;left:357px;top:542px;width:140px;height:140px;border-radius:50%;border:3px solid var(--white);display:flex;align-items:center;justify-content:center;text-align:center;padding:16px;font-size:15px;line-height:1.2;color:var(--white)}
.contact{position:absolute;left:210px;top:680px;display:flex;flex-direction:column;gap:3px}
.contact__row{display:flex;align-items:center;gap:8px}
.contact__phone{font-weight:700;font-size:20px;color:var(--white);line-height:1}
.contact__address{font-size:12.5px;line-height:1.25;font-weight:700;color:var(--white)}
.icon{flex:none;display:block}
</style>
</head>
<body>

<section class="flyer flyer--front">
  <svg class="band" style="top:0;height:170px" viewBox="0 0 527 170" preserveAspectRatio="none" aria-hidden="true">
    <path d="M0 0H527V128L500 122 470 136 430 118 380 132 330 112 290 126 240 108 200 122 150 104 100 116 60 100 30 112 0 98Z" fill="var(--red)"/>
    <path d="M0 0H150L120 20 80 14 40 34 0 30Z" fill="var(--ink)"/>
  </svg>
  <h1 class="display front__title front__title--one">Challenge</h1>
  <h1 class="display front__title front__title--two">Yourself...</h1>
  <p class="front__lead">Teaching is the highest form of learning.<br>Be a part of a professional, dedicated team,<br>delivering the highest level Kung Fu...</p>

  <span class="display vertical v-copper">Copper</span>
  <span class="display vertical v-heron">Heron</span>
  <div class="display emblem">Copper Heron Martial Arts</div>
  <span class="display vertical v-martial">Martial</span>
  <span class="display vertical v-arts">Arts</span>

  <svg class="band" style="bottom:0;height:95px" viewBox="0 0 527 95" preserveAspectRatio="none" aria-hidden="true">
    <path d="M0 14 40 6 90 18 150 4 210 16 270 2 330 14 390 0 450 12 527 4V95H0Z" fill="var(--red)"/>
  </svg>
  <div class="display front__web">
    <svg class="icon" width="32" height="32" viewBox="0 0 32 32" aria-hidden="true">
      <circle cx="16" cy="16" r="14" fill="#666" stroke="#888" stroke-width="2"/>
      <g fill="none" stroke="#ccc" stroke-width="1.6"><ellipse cx="16" cy="16" rx="6" ry="14"/><path d="M2 16H30M5 9H27M5 23H27"/></g>
    </svg>
    copperheron.com.au
  </div>
</section>

<section class="flyer flyer--back">
  <svg class="band" style="top:0;height:90px" viewBox="0 0 527 90" preserveAspectRatio="none" aria-hidden="true">
    <path d="M0 0H260L230 12 200 6 170 22 130 14 90 30 50 24 0 40Z" fill="var(--red)"/>
  </svg>
  <h1 class="display back__seeking">Seeking</h1>
  <h2 class="display back__role">Martial Arts Instructors!</h2>
  <p class="back__intro">We train in one of the world's most effective martial art systems, Choy Li Fut Kung Fu. As an instructor, you will teach both beginner &amp; intermediate level Kung Fu skills to adults &amp; children at Copper Heron Martial Arts, Brisbane's premier martial arts school.</p>

  <div class="photo" role="img" aria-label="Photo of an instructor leading a kung fu class"></div>

  <svg class="band" style="top:172px;height:210px" viewBox="0 0 527 210" preserveAspectRatio="none" aria-hidden="true">
    <defs><linearGradient id="dutiesBand" x1="0" x2="1"><stop offset="0" stop-color="#c8141d"/><stop offset=".7" stop-color="#c8141d"/><stop offset="1" stop-color="#8e0b12"/></linearGradient></defs>
    <path d="M0 40 60 30 120 42 190 26 260 38 330 22 400 34 470 20 527 28V170L480 182 420 168 360 186 300 172 240 190 180 176 120 194 60 180 0 196Z" fill="url(#dutiesBand)"/>
  </svg>

  <div class="block block--duties">
    <h3 class="block__heading">As an instructor, you will:</h3>
    <ul>
      <li>Teach fundamentals to children &amp; adults of all ages and abilities</li>
      <li>Progress student's martial arts and life skills</li>
      <li>Deliver fun and engaging classes</li>
      <li>Develop and grow your martial arts skills at an advanced level and pace</li>
    </ul>
  </div>

  <div class="block block--rewards">
    <h3 class="block__heading">In return, you will receive</h3>
    <ul>
      <li>Your training tuition, which includes our high level instructor training program, until qualified</li>
      <li>A weekly 1 on 1 with our very own Sifu, as well as one hour training sessions, twice a week , with our team.</li>
    </ul>
  </div>

  <div class="motto">
    <p class="motto__intro">At CHMA our motto is</p>
    <p class="motto__line">"Challenge Yourself..</p>
    <p class="motto__line motto__line--red">For Life!"</p>
  </div>

  <svg class="band" style="bottom:0;height:90px" viewBox="0 0 527 90" preserveAspectRatio="none" aria-hidden="true">
    <path d="M0 30 70 14 140 26 200 8 270 22 340 6 410 18 470 4 527 10V90H0Z" fill="var(--red)"/>
  </svg>

  <div class="display badge">Copper Heron Martial Arts</div>

  <div class="contact">
    <div class="contact__row">
      <svg class="icon" width="18" height="18" viewBox="0 0 18 18" aria-hidden="true"><circle cx="9" cy="9" r="9" fill="var(--white)"/><path d="M5.5 4.5 7.5 4 8.5 6.5 7.3 7.5C7.8 8.8 9 10 10.3 10.6L11.3 9.4 13.8 10.5 13.4 12.5C9 12.8 5 8.5 5.5 4.5Z" fill="var(--red)"/></svg>
      <span class="contact__phone">0417 863 120</span>
    </div>
    <div class="contact__row">
      <svg class="icon" width="18" height="18" viewBox="0 0 18 18" aria-hidden="true"><circle cx="9" cy="9" r="9" fill="var(--white)"/><path d="M9 3.5C6.8 3.5 5.3 5 5.3 7c0 2.6 3.7 7 3.7 7s3.7-4.4 3.7-7c0-2-1.5-3.5-3.7-3.5Z" fill="var(--red)"/><circle cx="9" cy="7" r="1.3" fill="var(--white)"/></svg>
      <span class="contact__address">The Hub Oakvale 27 Riverbend Rd.<br>Shop 112, Oakvale QLD 4120, Australia</span>
    </div>
  </div>
</section>

</body>
</html>
```